Business Card design for construction company

I would like a business card design for a construction company - Harlow Constructions. I have attached the ai logo file for use. I would like the card to be very smart and clean and incorporate only white and the two colours in the logo. I would like the card to have two sides. One side can just have the logo, the other with the relevant information.

Target Market(s)

Building and Construction Clients

Industry/Entity Type

Business

Contact Information for Business Card

Name: Tom Pardoe
Company: Harlow Constructions Pty Limited
Address: 14 Mallee Crescent Carrow Vale 2093
Phone: 0427 531 068
Email: tomp@harlowbuild-example.com.au

Font styles to use
Serif
Sans Serif

Requirements
Must have
• Details noted above
• Logo as provided
• Colours as in logo
• Square edges
• A font that compliments the logo
Should not have
• Any colour other than white and those in logo
• Rounded edges

```html
<!DOCTYPE html>
<html lang="en">
<head>
<meta charset="utf-8">
<title>Harlow Constructions – Business Card</title>
<link rel="stylesheet" href="https://fonts.googleapis.com/css2?family=Montserrat:wght@300;400;700&display=swap">
<style>
  :root {
    --brand-blue: #00aeef;
    --brand-charcoal: #58595b;
    --card-border: #5a5a5a;
    --paper: #ffffff;
    --text-dark: #4d4d4f;
  }
  * { box-sizing: border-box; margin: 0; padding: 0; }
  html, body {
    width: 1200px;
    height: 311px;
    overflow: hidden;
    background: var(--paper);
  }
  body {
    position: relative;
    font-family: "Montserrat", "Helvetica Neue", Arial, sans-serif;
  }

  /* Front side */
  .card-front {
    position: absolute;
    left: 0;
    top: 0;
    width: 538px;
    height: 311px;
    background: var(--brand-blue);
    display: flex;
    align-items: center;
    justify-content: center;
  }
  .brand-name {
    color: var(--paper);
    font-weight: 400;
    font-size: 21px;
    letter-spacing: 3px;
    text-transform: uppercase;
    margin-left: 30px;
  }

  /* Back side */
  .card-back {
    position: absolute;
    left: 660px;
    top: 0;
    width: 540px;
    height: 311px;
    background: var(--paper);
    border: 2px solid var(--card-border);
  }
  .holder-name {
    position: absolute;
    left: 35px;
    top: 28px;
    font-size: 38px;
    line-height: 1;
    color: var(--text-dark);
    text-transform: uppercase;
    letter-spacing: 0.5px;
  }
  .holder-name .first { font-weight: 700; }
  .holder-name .last { font-weight: 300; }

  .contact-list {
    position: absolute;
    left: 224px;
    top: 180px;
    list-style: none;
  }
  .contact-item {
    display: flex;
    align-items: center;
    height: 26px;
  }
  .contact-icon {
    width: 25px;
    height: 26px;
    display: flex;
    align-items: center;
    justify-content: center;
    margin-right: 14px;
    flex-shrink: 0;
  }
  .contact-icon.is-blue { background: var(--brand-blue); }
  .contact-icon.is-dark { background: var(--brand-charcoal); }
  .contact-icon svg { width: 12px; height: 12px; fill: var(--paper); }
  .contact-text {
    font-size: 14px;
    font-weight: 400;
    color: var(--text-dark);
    white-space: nowrap;
  }
</style>
</head>
<body>
  <section class="card-front">
    <div class="brand-name">Harlow Constructions</div>
  </section>

  <section class="card-back">
    <h1 class="holder-name"><span class="first">Tom</span> <span class="last">Pardoe</span></h1>

    <ul class="contact-list">
      <li class="contact-item">
        <span class="contact-icon is-blue">
          <svg viewBox="0 0 24 24" aria-hidden="true"><path d="M6.6 10.8a15.1 15.1 0 0 0 6.6 6.6l2.2-2.2a1 1 0 0 1 1-.25 11.4 11.4 0 0 0 3.6.57 1 1 0 0 1 1 1V20a1 1 0 0 1-1 1A17 17 0 0 1 3 4a1 1 0 0 1 1-1h3.5a1 1 0 0 1 1 1c0 1.25.2 2.45.57 3.6a1 1 0 0 1-.25 1z"/></svg>
        </span>
        <span class="contact-text">0427 531 068</span>
      </li>
      <li class="contact-item">
        <span class="contact-icon is-dark">
          <svg viewBox="0 0 24 24" aria-hidden="true"><path d="M2 5h20v2l-10 6L2 7z"/><path d="M2 9l10 6 10-6v10H2z"/></svg>
        </span>
        <span class="contact-text">tomp@harlowbuild-example.com.au</span>
      </li>
      <li class="contact-item">
        <span class="contact-icon is-blue">
          <svg viewBox="0 0 24 24" aria-hidden="true"><path d="M12 2a10 10 0 1 0 0 20 10 10 0 0 0 0-20zm7.9 9h-3.4a15 15 0 0 0-1.4-6.3A8 8 0 0 1 19.9 11zM12 4.1c.9 1.2 2.3 3.6 2.5 6.9h-5C9.7 7.7 11.1 5.3 12 4.1zM8.9 4.7A15 15 0 0 0 7.5 11H4.1a8 8 0 0 1 4.8-6.3zM4.1 13h3.4a15 15 0 0 0 1.4 6.3A8 8 0 0 1 4.1 13zm7.9 6.9c-.9-1.2-2.3-3.6-2.5-6.9h5c-.2 3.3-1.6 5.7-2.5 6.9zm3.1-.6a15 15 0 0 0 1.4-6.3h3.4a8 8 0 0 1-4.8 6.3z"/></svg>
        </span>
        <span class="contact-text">harlowbuild-example.com.au</span>
      </li>
      <li class="contact-item">
        <span class="contact-icon is-dark">
          <svg viewBox="0 0 24 24" aria-hidden="true"><path d="M12 2a7 7 0 0 0-7 7c0 5.2 7 13 7 13s7-7.8 7-13a7 7 0 0 0-7-7zm0 9.5A2.5 2.5 0 1 1 12 6.5a2.5 2.5 0 0 1 0 5z"/></svg>
        </span>
        <span class="contact-text">14 Mallee Crescent Carrow Vale 2093</span>
      </li>
    </ul>
  </section>
</body>
</html>
```